Business Card Upgrade

I have designed our business card using our new logo. I think it needs imporovements. We used to have two cards for our business. One card was for our software business, and the other was for our consulting business. We are now in the process of combining our websites, marketing, name, and a new logo.

Our goal is to have a really sharp professional logo. One reason I designed the card the way I did was that our Titles are sometimes long, and by separating the person's name and title, it shows up very well and the title can be adjusted no matter how long it is. Sometimes the title can be 4 or 5 words or more.

We really like our logo on black as it shows up very nice. Our PMS colors are as follows: 368C and 459C.

The Designer that will be working with us will need to deliver the following:

The front and back of the Business Card Design will need to be delivered in a high quality JPEG, and
The front and back of the Business Card Design in Illustrator Format .ai
Any fonts will need to be sent to us if they are not standard and are required to open the Illustrator file correctly.

To help us get a good idea of the card with a title, please use the title: " Director of Software Development "

NOTE: The chosen designer will be selected to design our new letterhead within 2 weeks from the closing of this contest.
Updates

To help us make sure the card design works with longer titles, please use the followign job title on the card:  

"Director of Software and Product Development"

 

ALL DESIGNERS:

1. I appreciate the different angles you are showing the cards, but please be sure and always show the direct view, so I can see the layout and what the person I hand the card will see.

2. Please do not use white.  Please use off white as I don't care for white cards and they get dirty easy and do not represent the designs well.

Dear Designers,

Please provide samples straight one as a viewer of the card will see.  Some of the angles that are presented make it impossible to tell how everything fits, and sometimes even makes areas look skewed. So, please provide a straight sample view.

Target Market(s)

Keystone 400 company executives such as Vice Presidents, and Directors

Industry/Entity Type

Software

Requirements
Must have
• Professional looking Card.

Our customers are Directors, Vice Presidents, and Presidents of companies as large as Keystone 400 companies. The card needs to get attention wile still looking professional.

Delivery of the finished product in Illustrator Format with any fonts needed to edit the text or open the file.

The card will be a heavy stock with a soft touch coating for that silk feel.

```html
<!DOCTYPE html>
<html lang="en">
<head>
<meta charset="utf-8">
<title>Harborline Trade Systems – Business Card</title>
<link href="https://fonts.googleapis.com/css2?family=Titillium+Web:wght@300;400;600&display=swap" rel="stylesheet">
<style>
  :root {
    --backdrop: #d9d9db;
    --card-black: #070807;
    --brand-green: #78be20;
    --brand-gold: #d8cf7c;
    --map-green: #1d5a26;
    --line-green: #2f6b22;
  }
  * { box-sizing: border-box; margin: 0; padding: 0; }
  html, body {
    width: 1200px; height: 900px; overflow: hidden;
    background: var(--backdrop);
    font-family: "Titillium Web", "Helvetica Neue", Arial, sans-serif;
  }
  .canvas {
    width: 1200px; height: 900px;
    display: flex; flex-direction: column; align-items: center; justify-content: center;
    gap: 56px;
  }
  .card {
    position: relative;
    width: 560px; height: 320px;
    background: var(--card-black);
    border-radius: 18px;
    overflow: hidden;
    box-shadow: 0 6px 18px rgba(0,0,0,.25);
  }

  /* Front */
  .front-artwork {
    position: absolute; inset: 0;
    background:
      radial-gradient(ellipse 60% 70% at 50% 45%, rgba(29,90,38,.0) 30%, rgba(29,90,38,.35) 60%, rgba(0,0,0,0) 85%),
      radial-gradient(ellipse 30% 45% at 28% 55%, rgba(29,90,38,.55), rgba(0,0,0,0) 70%),
      radial-gradient(ellipse 22% 35% at 72% 40%, rgba(29,90,38,.5), rgba(0,0,0,0) 70%),
      var(--card-black);
  }
  .front-brand {
    position: absolute; left: 0; right: 0; top: 118px;
    text-align: center;
  }
  .brand-name {
    color: var(--brand-green);
    font-weight: 600;
    letter-spacing: 1px;
    line-height: 1;
  }
  .front-brand .brand-name { font-size: 40px; }
  .front-web {
    position: absolute; left: 0; right: 0; top: 218px;
    text-align: center;
    color: var(--brand-green);
    font-size: 15px; letter-spacing: 2px;
  }

  /* Back */
  .back-artwork {
    position: absolute; right: 0; bottom: 0;
    width: 320px; height: 150px;
    background: radial-gradient(ellipse 90% 100% at 100% 100%, rgba(47,107,34,.45), rgba(0,0,0,0) 75%);
  }
  .back-brand {
    position: absolute; left: 34px; top: 38px;
  }
  .back-brand .brand-name { font-size: 26px; }
  .person {
    position: absolute; left: 34px; top: 118px;
  }
  .person-name {
    color: var(--brand-gold);
    font-size: 22px; font-weight: 300; letter-spacing: .5px;
    text-transform: uppercase;
    line-height: 1.1;
  }
  .person-title {
    color: var(--brand-green);
    font-size: 13.5px; font-weight: 400;
    margin-top: 2px;
  }
  .contact-list {
    position: absolute; left: 34px; top: 198px;
    list-style: none;
    color: var(--brand-gold);
    font-size: 15px; font-weight: 300;
  }
  .contact-list li { display: flex; align-items: center; gap: 9px; line-height: 24px; }
  .contact-list svg { width: 14px; height: 14px; fill: var(--brand-green); flex: none; }
  .address {
    position: absolute; left: 312px; top: 150px;
    padding-left: 14px;
    border-left: 1.5px solid var(--brand-green);
    color: var(--brand-gold);
    font-size: 13.5px; font-weight: 300; line-height: 21px;
  }
</style>
</head>
<body>
<main class="canvas">

  <section class="card card-front" aria-label="Business card front">
    <div class="front-artwork" role="img" aria-label="Dark green world map with radiating fine line pattern on black"></div>
    <div class="front-brand"><span class="brand-name">Harborline Trade Systems</span></div>
    <p class="front-web">www.harborlinetrade.com</p>
  </section>

  <section class="card card-back" aria-label="Business card back">
    <div class="back-artwork" role="img" aria-label="Faint green radiating line pattern"></div>
    <div class="back-brand"><span class="brand-name">Harborline Trade Systems</span></div>

    <div class="person">
      <p class="person-name">Dana Whitfield</p>
      <p class="person-title">Director of Software and Product Development</p>
    </div>

    <ul class="contact-list">
      <li>
        <svg viewBox="0 0 14 14" aria-hidden="true"><path d="M3 1h2.2l1 3-1.4 1.1a7 7 0 0 0 3.1 3.1L9 6.8l3 1V10a1.5 1.5 0 0 1-1.6 1.5C5.6 11.2 2.8 8.4 2.5 3.6A1.5 1.5 0 0 1 3 1z"/></svg>
        (555) 014-3725
      </li>
      <li>
        <svg viewBox="0 0 14 14" aria-hidden="true"><rect x="4" y="1" width="6" height="4"/><rect x="1" y="5" width="12" height="5" rx="1"/><rect x="4" y="9" width="6" height="4"/></svg>
        (555) 014-3727
      </li>
      <li>
        <svg viewBox="0 0 14 14" aria-hidden="true"><path d="M1 3h12v8H1z M1.5 3.5 7 8l5.5-4.5" stroke="#070807" stroke-width="1"/></svg>
        info@harborlinetrade.com
      </li>
    </ul>

    <address class="address">
      Harborline Trade Systems<br>
      418 Cedar Quay Road<br>
      Larkport, Alabama 36690
    </address>
  </section>

</main>
</body>
</html>
```